Dog care service needs business card design

Our company is Paws Harbour. We provide care for dogs while their owners are away, either through home visits or a holiday stay in the homes of carefully selected minders. Our existing website & Chatterbook cover should provide all the colour cues for our business cards - namely blues, blondes and grey. We have an existing logo (provided).

www.pawsharbourcare.example.au
www.facebook.com/pawsharbourcareau

We wish to clearly communicate our three areas of service "dog minding, home visits, dog walking".

We would like to have the files ready for upload to Printlyne (or similar) for immediate printing.

Target Market(s)

Dog owners who love their dogs like family

Industry/Entity Type

Business

Contact Information for Business Card

Paws Harbour
Ph: 0417 358 904

Font styles to use
Sans Serif

Colors
33a6d7
3176b5

Requirements
Must have
• Logo
• Telephone number
• website
• "Dog minding, home visits, dog walking"
Should not have
• any additional illustrations beyond the logo.

```html
<!DOCTYPE html>
<html lang="en">
<head>
<meta charset="utf-8">
<title>Paws Harbour – Business Card</title>
<link href="https://fonts.googleapis.com/css2?family=Arimo:wght@400;500&display=swap" rel="stylesheet">
<style>
  :root {
    --bg: #e9e7e3;
    --card: #fbfbfb;
    --ink: #4a5566;
    --ink-soft: #5d6675;
    --blue-deep: #3176b5;
    --blue-bright: #33a6d7;
    --icon: #4fb3de;
    --arc: #46505f;
  }
  * { box-sizing: border-box; margin: 0; padding: 0; }
  html, body { width: 1200px; height: 858px; overflow: hidden; }
  body {
    background: var(--bg);
    font-family: "Arimo", Arial, sans-serif;
    display: flex;
    align-items: center;
    justify-content: center;
    gap: 40px;
  }
  .card {
    position: relative;
    width: 540px;
    height: 310px;
    background: var(--card);
    box-shadow: 0 6px 18px rgba(0,0,0,0.15);
    overflow: hidden;
    color: var(--ink);
  }
  .swoosh { position: absolute; inset: 0; width: 100%; height: 100%; }

  .brand {
    display: flex;
    align-items: center;
    gap: 10px;
    font-size: 34px;
    font-weight: 500;
    color: var(--ink);
    letter-spacing: -0.5px;
  }
  .brand-dot {
    width: 14px; height: 14px; border-radius: 50%;
    background: var(--blue-bright);
  }
  .card-front .brand { position: absolute; left: 34px; top: 40px; }

  .contact {
    position: absolute;
    right: 28px;
    top: 36px;
    text-align: right;
  }
  .contact-name {
    font-size: 24px;
    color: var(--ink-soft);
    margin-bottom: 14px;
  }
  .contact-line {
    display: flex;
    justify-content: flex-end;
    align-items: center;
    gap: 8px;
    font-size: 12px;
    color: var(--ink-soft);
    line-height: 22px;
  }
  .contact-line svg { width: 14px; height: 14px; fill: var(--icon); flex: none; }

  .person {
    position: absolute;
    left: 30px;
    bottom: 26px;
    color: #fff;
  }
  .person-name { font-size: 22px; }
  .person-role { font-size: 14px; opacity: 0.9; margin-top: 2px; padding-left: 22px; }

  .card-back {
    display: flex;
    flex-direction: column;
    align-items: center;
    justify-content: center;
    gap: 18px;
  }
  .card-back .brand { font-size: 40px; }
  .services { font-size: 15px; color: var(--ink); letter-spacing: 0.2px; }
</style>
</head>
<body>
  <section class="card card-front">
    <svg class="swoosh" viewBox="0 0 540 310" preserveAspectRatio="none" aria-hidden="true">
      <defs>
        <linearGradient id="blueBand" x1="0" y1="0" x2="1" y2="0">
          <stop offset="0" stop-color="#3176b5"/>
          <stop offset="1" stop-color="#33a6d7"/>
        </linearGradient>
      </defs>
      <path d="M0,178 Q220,262 470,310 L0,310 Z" fill="url(#blueBand)"/>
      <path d="M0,158 Q230,250 520,310" fill="none" stroke="#46505f" stroke-width="7"/>
      <path d="M0,168 Q225,256 495,310" fill="none" stroke="#ffffff" stroke-width="3"/>
    </svg>

    <div class="brand"><span class="brand-dot"></span>Paws Harbour</div>

    <div class="contact">
      <div class="contact-name">Paws Harbour</div>
      <div class="contact-line">0417 358 904
        <svg viewBox="0 0 16 16"><path d="M3 1h3l1.5 4-2 1.3a9 9 0 0 0 4.2 4.2L11 8.5l4 1.5v3a2 2 0 0 1-2 2A12 12 0 0 1 1 3a2 2 0 0 1 2-2z"/></svg>
      </div>
      <div class="contact-line">www.pawsharbourcare.example.au
        <svg viewBox="0 0 16 16"><path d="M8 1a7 7 0 1 0 0 14A7 7 0 0 0 8 1zm0 1.5c.9 1 1.5 2.6 1.7 4.5H6.3C6.5 5.1 7.1 3.5 8 2.5zM6.3 9h3.4c-.2 1.9-.8 3.5-1.7 4.5-.9-1-1.5-2.6-1.7-4.5zM2.6 9h2.2c.1 1.5.5 2.9 1 3.9A5.5 5.5 0 0 1 2.6 9zm8.6 0h2.2a5.5 5.5 0 0 1-3.2 3.9c.5-1 .9-2.4 1-3.9zM2.6 7a5.5 5.5 0 0 1 3.2-3.9c-.5 1-.9 2.4-1 3.9zm8.6 0c-.1-1.5-.5-2.9-1-3.9A5.5 5.5 0 0 1 13.4 7z"/></svg>
      </div>
      <div class="contact-line">info@pawsharbourcare.example.au
        <svg viewBox="0 0 16 16"><path d="M1 3h14v10H1zM2.5 4.5 8 9l5.5-4.5z"/></svg>
      </div>
      <div class="contact-line">Kellyvale, New South Wales, Australia 2790
        <svg viewBox="0 0 16 16"><path d="M8 1 1 7.5h2V15h4v-4h2v4h4V7.5h2z"/></svg>
      </div>
    </div>

    <div class="person">
      <div class="person-name">Employee Name</div>
      <div class="person-role">Managing Director</div>
    </div>
  </section>

  <section class="card card-back">
    <div class="brand"><span class="brand-dot"></span>Paws Harbour</div>
    <p class="services">Dog minding | home visits | dog walking</p>
  </section>
</body>
</html>
```